Engineering Consultant Business Card

I'm starting a new business as a high-end engineering consultant in a niche field. I've attached the jpg for my logo plus the branding guideline document that I've been following. You can see my business website here: www.tarvikworks.com
I'd like a business card that has the logo on one side, then the other side has (in any order): Tarvik Works, Inc.
Dana Whitlock
President and Chief EMC Engineer
www.tarvikworks.com
dana@tarvikworks.com
Optional: motto "We will solve your EMC problems as early as possible—ideally before they even start."
I'm not planning on including a phone number
Target Market(s)
Businesses, especially makers of electronics hardware
Industry/Entity Type
Electrical engineering
Contact Information for Business Card
Company name, my name, website, email

```html
<!DOCTYPE html>
<html lang="en">
<head>
<meta charset="utf-8">
<title>Tarvik Works – Business Card</title>
<link href="https://fonts.googleapis.com/css2?family=Roboto:wght@300;400;500&display=swap" rel="stylesheet">
<style>
  :root {
    --backdrop: #e4e4e4;
    --card-blue: #2f4795;
    --ink: #ffffff;
  }
  * { box-sizing: border-box; margin: 0; padding: 0; }
  html, body {
    width: 1200px; height: 1200px; overflow: hidden;
    background: var(--backdrop);
    font-family: "Roboto", Arial, sans-serif;
    color: var(--ink);
  }
  .canvas { position: relative; width: 1200px; height: 1200px; }
  .card {
    position: absolute; left: 165px; width: 872px; height: 509px;
    background: var(--card-blue);
  }
  .card--front { top: 70px; }
  .card--back { top: 621px; }

  /* front */
  .brand-mark {
    position: absolute; left: 91px; top: 145px; width: 113px; height: 222px;
    display: flex; flex-direction: column; align-items: center; justify-content: center; gap: 14px;
  }
  .brand-mark__dot { width: 44px; height: 44px; border-radius: 50%; background: var(--ink); }
  .brand-mark__name {
    writing-mode: vertical-rl; transform: rotate(180deg);
    font-weight: 500; font-size: 30px; letter-spacing: 0.5px; white-space: nowrap;
  }
  .company-name {
    position: absolute; left: 226px; top: 105px; width: 40px; height: 300px;
    display: flex; align-items: center; justify-content: center;
  }
  .company-name span {
    writing-mode: vertical-rl; transform: rotate(180deg);
    font-weight: 400; font-size: 28px; letter-spacing: 0.3px; white-space: nowrap;
  }
  .divider {
    position: absolute; left: 385px; top: 64px; width: 3px; height: 381px; background: var(--ink);
  }
  .person {
    position: absolute; right: 50px; top: 148px; text-align: right;
  }
  .person__name { font-weight: 500; font-size: 37px; letter-spacing: 0.4px; line-height: 1; }
  .person__title { font-weight: 300; font-size: 21px; margin-top: 12px; line-height: 1; }
  .contact {
    position: absolute; right: 50px; top: 300px; list-style: none; text-align: right;
  }
  .contact__item {
    display: flex; align-items: center; justify-content: flex-end; gap: 12px;
    font-weight: 300; font-size: 24px; line-height: 34px;
  }
  .contact__icon { width: 14px; height: 14px; fill: var(--ink); flex: none; }

  /* back */
  .back-mark {
    position: absolute; left: 0; right: 0; top: 156px; height: 163px;
    display: flex; align-items: center; justify-content: center; gap: 22px;
  }
  .back-mark__dot { width: 64px; height: 64px; border-radius: 50%; background: var(--ink); }
  .back-mark__name { font-weight: 500; font-size: 60px; letter-spacing: 1px; white-space: nowrap; }
</style>
</head>
<body>
<main class="canvas">
  <section class="card card--front" aria-label="Business card front">
    <div class="brand-mark">
      <span class="brand-mark__dot"></span>
      <span class="brand-mark__name">Tarvik Works</span>
    </div>
    <div class="company-name"><span>Tarvik Works, Inc.</span></div>
    <div class="divider"></div>
    <div class="person">
      <h1 class="person__name">DANA WHITLOCK</h1>
      <p class="person__title">President and Chief EMC Engineer</p>
    </div>
    <ul class="contact">
      <li class="contact__item">www.tarvikworks.com
        <svg class="contact__icon" viewBox="0 0 16 16" aria-hidden="true"><circle cx="8" cy="8" r="7" fill="none" stroke="#fff" stroke-width="1.6"/><ellipse cx="8" cy="8" rx="3" ry="7" fill="none" stroke="#fff" stroke-width="1.4"/><line x1="1" y1="8" x2="15" y2="8" stroke="#fff" stroke-width="1.4"/></svg>
      </li>
      <li class="contact__item">dana@tarvikworks.com
        <svg class="contact__icon" viewBox="0 0 16 16" aria-hidden="true"><path d="M8 0.5a5.5 5.5 0 0 0-5.5 5.5c0 4 5.5 9.5 5.5 9.5s5.5-5.5 5.5-9.5A5.5 5.5 0 0 0 8 0.5zm0 7.6a2.1 2.1 0 1 1 0-4.2 2.1 2.1 0 0 1 0 4.2z"/></svg>
      </li>
    </ul>
  </section>

  <section class="card card--back" aria-label="Business card back">
    <div class="back-mark">
      <span class="back-mark__dot"></span>
      <span class="back-mark__name">Tarvik Works</span>
    </div>
  </section>
</main>
</body>
</html>
```